yourSmileCare Brookvale Business Card

Please design a two sided business card that is Elegant and Professional
Add subtle elegant patterns to suit Spot UV printing/ or raised printing

Name: Dr Marcus T. Fenwick
Qualification: BDSc (QLD)
Title: Dental Surgeon, Clinical Director
Company: yourSmileCare Brookvale
Phone: (02) 7593 2268
Address: Shop 7/18-20 Lindon Ave Brookvale 2097
email: info@yoursmilecarebrookvale.com.au
Facebook: linkloop.com/yoursmilecarebrookvale

Motto:
Quality dentistry you can trust

Description of services (not compulsory):
Preventative Dentistry | General Dentistry
Cosmetic Dentistry | Teeth Whitening
Crown and Bridge | Root Canal Therapy
Veneers | Clearvono | Orthodontics
Emergency Dental Care | After Hours

Personalised Treatment Plans
Transparent Fees

Please make sure card is elegant and professional

Target Market(s)

general population, patients,
Dental sales companies, other professions

Industry/Entity Type

Dental Clinic

Contact Information for Business Card

Name: Dr Marcus T. Fenwick
Qualification: BDSc (QLD)
Phone: (02) 7593 2268
Address: Shop 7/18-20 Lindon Ave Brookvale

Motto:

Description of services (not compulsory)

Transparent Fees

Image of dental surgery optional

Please make sure card is elegant and profession

Requirements
Must have
• Logo
• Name, Title (next to name), Business
• Phone, address, facbeook
• Must have stylish design to suit SPOT UV reflective printing
Nice to have
• Subtle elegant patterns which will have Spot UV on them when printed
• Colours to match logo colour
• Description of services
Should not have
• Small fonts that are hard to read
• DO NOT PUT IMAGES OF DENTAL INSTRUMENTS OR TEETH PLEASE

```html
<!DOCTYPE html>
<html lang="en">
<head>
<meta charset="utf-8">
<title>yourSmileCare Brookvale – Business Card</title>
<link href="https://fonts.googleapis.com/css2?family=Open+Sans:ital,wght@0,400;0,600;0,700;1,600&display=swap" rel="stylesheet">
<style>
  :root {
    --bg: #8c8c8c;
    --bg-light: #b4b4b4;
    --green-dark: #0b7a34;
    --green-mid: #3fa83a;
    --green-lime: #93d94b;
    --ink: #1f1f1f;
    --grey: #8a8a8a;
    --white: #ffffff;
    --tab: #141414;
  }
  * { box-sizing: border-box; margin: 0; padding: 0; }
  html, body {
    width: 1200px; height: 960px; overflow: hidden;
    font-family: "Open Sans", Arial, sans-serif;
  }
  .canvas {
    position: relative; width: 1200px; height: 960px;
    background: radial-gradient(ellipse at 50% 45%, var(--bg-light), var(--bg));
  }
  .card {
    position: absolute; top: 320px; width: 560px; height: 320px;
    overflow: hidden; border-radius: 3px;
    box-shadow: 0 10px 28px rgba(0,0,0,.28);
  }
  .card--back { left: 26px; background: linear-gradient(135deg, var(--green-dark) 0%, var(--green-mid) 50%, var(--green-lime) 100%); color: var(--white); }
  .card--front { left: 614px; background: var(--white); color: var(--ink); }

  /* brand name */
  .brand { position: absolute; }
  .brand__name { font-weight: 600; font-size: 27px; letter-spacing: -.3px; line-height: 1; }
  .brand__place { font-weight: 400; font-size: 14px; letter-spacing: 3px; margin-top: 4px; }

  /* back */
  .card--back .brand { left: 30px; top: 128px; }
  .services {
    position: absolute; left: 210px; top: 76px; width: 340px;
    text-align: center; font-size: 13px; line-height: 20px; font-weight: 600;
  }
  .services__extra { margin-top: 8px; }
  .services__extra li { list-style: none; }
  .services__extra li::before { content: "\2713"; margin-right: 6px; }

  /* front */
  .card--front .brand { left: 30px; top: 28px; }
  .card--front .brand__name { color: var(--green-mid); }
  .card--front .brand__place { color: var(--grey); }
  .motto { position: absolute; left: 30px; top: 86px; font-style: italic; font-weight: 600; font-size: 13px; line-height: 17px; }
  .person { position: absolute; right: 26px; top: 66px; text-align: right; }
  .person__name { font-size: 20px; font-weight: 700; }
  .person__qual { font-size: 10px; font-weight: 400; color: var(--grey); margin-left: 4px; }
  .person__title { font-size: 13px; margin-top: 2px; }

  .band {
    position: absolute; left: 0; right: 0; top: 152px; bottom: 0;
    background: linear-gradient(100deg, var(--green-dark) 0%, var(--green-mid) 55%, var(--green-lime) 100%);
    color: var(--white);
  }
  .tab {
    position: absolute; left: 0; top: 134px; width: 214px; height: 30px;
    background: var(--tab); border-radius: 0 10px 0 0; color: var(--white);
    font-size: 12.5px; font-weight: 600; padding: 6px 0 0 22px;
  }
  .tab__dot { position: absolute; right: 10px; top: 10px; width: 10px; height: 10px; border-radius: 50%; background: var(--green-lime); }
  .phone { position: absolute; left: 20px; top: 30px; font-size: 22px; font-weight: 700; display: flex; align-items: center; gap: 8px; }
  .address { position: absolute; left: 20px; top: 72px; font-size: 12.5px; line-height: 17px; display: flex; gap: 8px; }
  .links { position: absolute; left: 262px; top: 26px; list-style: none; font-size: 12.5px; }
  .links li { display: flex; align-items: center; gap: 8px; height: 28px; }
  .icon { width: 18px; height: 18px; flex: none; }
  .icon--round { border-radius: 50%; background: var(--white); display: flex; align-items: center; justify-content: center; }
</style>
</head>
<body>
<main class="canvas">

  <section class="card card--back" aria-label="Business card back">
    <div class="brand">
      <p class="brand__name">yourSmileCare</p>
      <p class="brand__place">BROOKVALE</p>
    </div>
    <div class="services">
      <p>Preventative Dentistry | General Dentistry</p>
      <p>Cosmetic Dentistry | Teeth Whitening</p>
      <p>Crown and Bridge | Root Canal Therapy</p>
      <p>Veneers | Clearvono | Orthodontics</p>
      <p>Emergency Dental Care | After Hours</p>
      <ul class="services__extra">
        <li>Personalised Treatment Plans</li>
        <li>Transparent Fees</li>
      </ul>
    </div>
  </section>

  <section class="card card--front" aria-label="Business card front">
    <div class="brand">
      <p class="brand__name">yourSmileCare</p>
      <p class="brand__place">BROOKVALE</p>
    </div>
    <p class="motto">Quality dentistry<br>you can trust</p>
    <div class="person">
      <p class="person__name">Dr Marcus T. Fenwick<span class="person__qual">BDSc (QLD)</span></p>
      <p class="person__title">Dental Surgeon, Clinical Director</p>
    </div>

    <div class="band">
      <p class="phone">
        <svg class="icon" viewBox="0 0 24 24" aria-hidden="true"><path fill="#fff" d="M6.6 10.8c1.4 2.8 3.8 5.1 6.6 6.6l2.2-2.2c.3-.3.7-.4 1-.2 1.1.4 2.3.6 3.6.6.6 0 1 .4 1 1V20c0 .6-.4 1-1 1C10.6 21 3 13.4 3 4c0-.6.4-1 1-1h3.5c.6 0 1 .4 1 1 0 1.3.2 2.5.6 3.6.1.3 0 .7-.2 1z"/></svg>
        <span>(02) 7593 2268</span>
      </p>
      <p class="address">
        <svg class="icon" viewBox="0 0 24 24" aria-hidden="true"><path fill="none" stroke="#fff" stroke-width="2" d="M12 22s7-7.2 7-12.5A7 7 0 0 0 5 9.5C5 14.8 12 22 12 22z"/><circle cx="12" cy="9.5" r="2.5" fill="none" stroke="#fff" stroke-width="2"/></svg>
        <span>Shop 7/18-20 Lindon Ave<br>Brookvale 2097</span>
      </p>
      <ul class="links">
        <li><span class="icon icon--round"><svg width="11" height="11" viewBox="0 0 24 24" aria-hidden="true"><rect x="2" y="5" width="20" height="14" rx="2" fill="none" stroke="#3fa83a" stroke-width="2.5"/><path d="M2 6l10 7 10-7" fill="none" stroke="#3fa83a" stroke-width="2.5"/></svg></span><span>info@yoursmilecarebrookvale.com.au</span></li>
        <li><span class="icon icon--round"><svg width="11" height="11" viewBox="0 0 24 24" aria-hidden="true"><circle cx="12" cy="12" r="9" fill="none" stroke="#3fa83a" stroke-width="2.5"/><path d="M3 12h18M12 3c3 3 3 15 0 18M12 3c-3 3-3 15 0 18" fill="none" stroke="#3fa83a" stroke-width="2"/></svg></span><span>yoursmilecarebrookvale.com.au</span></li>
        <li><span class="icon icon--round" aria-hidden="true"></span><span>linkloop.com/<strong>yoursmilecarebrookvale</strong></span></li>
      </ul>
    </div>
    <p class="tab">yourSmileCare Brookvale<span class="tab__dot"></span></p>
  </section>

</main>
</body>
</html>
```